Front and content page design for Fitness Cookbook

I am looking for someone to Design a front cover for a Recipe book and also create an amazing layout for the book.

Its for a corporate seminar so has to be eye catching, professional and bold.

Content is complete

Target Market(s)

Industry/Entity Type

Health And Wellness

Font styles to use
Sans Serif

Requirements
Must have
• Eye catching, professional and bold.
• By Dorian as stated on the document
• Must have Velmora Athletics Logo on it.

```html
<!DOCTYPE html>
<html lang="en">
<head>
<meta charset="utf-8">
<title>Cookbook Cover — Velmora Athletics</title>
<link href="https://fonts.googleapis.com/css2?family=Oswald:wght@300;500;700&display=swap" rel="stylesheet">
<style>
  :root {
    --brand-blue: #2b4796;
    --brand-orange: #f7941e;
    --paper: #ffffff;
    --ink: #3a3a3a;
  }
  html, body {
    margin: 0;
    padding: 0;
    overflow: hidden;
    background: var(--paper);
  }
  .cover {
    position: relative;
    width: 849px;
    height: 1200px;
    background: var(--paper);
    overflow: hidden;
    font-family: "Oswald", sans-serif;
  }
  .brand {
    position: absolute;
    top: 172px;
    left: 0;
    width: 100%;
    display: flex;
    justify-content: center;
    align-items: center;
    gap: 14px;
  }
  .brand-dot {
    width: 46px;
    height: 46px;
    border-radius: 50%;
    background: var(--brand-orange);
  }
  .brand-name {
    font-family: "Oswald", sans-serif;
    font-weight: 700;
    font-size: 34px;
    letter-spacing: 1px;
    color: var(--brand-blue);
    text-transform: uppercase;
  }
  .band {
    position: absolute;
    left: 0;
    width: 100%;
    display: flex;
    justify-content: center;
    align-items: flex-end;
    overflow: hidden;
  }
  .band--blue {
    top: 362px;
    height: 218px;
    background: var(--brand-blue);
  }
  .band--orange {
    top: 580px;
    height: 240px;
    background: var(--brand-orange);
  }
  .title-word {
    font-family: "Oswald", sans-serif;
    font-weight: 300;
    font-size: 258px;
    line-height: 0.78;
    color: var(--paper);
    letter-spacing: -2px;
    text-transform: uppercase;
    transform: scaleX(0.9);
  }
  .band--blue .title-word { margin-bottom: 4px; }
  .band--orange .title-word { margin-bottom: 6px; }
  .byline {
    position: absolute;
    top: 972px;
    left: 0;
    width: 100%;
    text-align: center;
    font-family: "Oswald", sans-serif;
    font-weight: 500;
    font-size: 38px;
    color: var(--ink);
  }
</style>
</head>
<body>
  <main class="cover">
    <header class="brand">
      <span class="brand-dot"></span>
      <span class="brand-name">Velmora Athletics</span>
    </header>

    <h1 class="title">
      <span class="band band--blue"><span class="title-word">Cook</span></span>
      <span class="band band--orange"><span class="title-word">Book</span></span>
    </h1>

    <p class="byline">by Dorian Kessler</p>
  </main>
</body>
</html>
```